Release Therapy business card that deals with the release of negative issues

I need a business card for my business called PEBBLES (A warm hearth to rest when you tire) ... I'm a therapist that deals with people releasing negative issues, by applying therapies that incorporate, hypnosis, aromatherapy and listen therapy..I like the colour green and soft blues...My idea is for a hand releasing butterflies, and incorporating soft clouds....
Target Market(s)
All people, all ages
Industry/Entity Type
Business
Contact Information for Business Card
PEBBLES"A Warm Hearth To Rest When You Tire"Yvette R BrockingtonRelease Therapist0411 743 781email: calmingpaths4you@quietmail.example
Requirements
Must have
- butterflies and soft clouds
Nice to have
- I like the decorative and script fonts for business name, and also my name
- Marisol T Fenwhistle...

```html
<!DOCTYPE html>
<html lang="en">
<head>
<meta charset="utf-8">
<title>PEBBLES – Release Therapist Business Card</title>
<link href="https://fonts.googleapis.com/css2?family=Kaushan+Script&family=Didact+Gothic&display=swap" rel="stylesheet">
<style>
  :root {
    --backdrop: #e8e5e2;
    --sky-top: #a9c8ea;
    --sky-mid: #c7dcf2;
    --sky-pale: #e6f0fa;
    --card-white: #ffffff;
    --title-blue: #1f4ea6;
    --tagline-blue: #1b3a78;
    --ink: #1d2f55;
    --butterfly-blue: #3aa6d8;
    --hand-tone: #e8b690;
  }
  * { box-sizing: border-box; margin: 0; padding: 0; }
  html, body {
    width: 1200px; height: 997px; overflow: hidden;
    background: var(--backdrop);
  }
  .stage { position: relative; width: 1200px; height: 997px; }
  .card {
    position: absolute; width: 520px; height: 300px;
    border-radius: 3px; overflow: hidden;
    box-shadow: 0 6px 18px rgba(0,0,0,0.12);
  }
  .card--back {
    left: 50px; top: 340px;
    background: linear-gradient(170deg, var(--sky-top) 0%, var(--sky-mid) 55%, var(--sky-pale) 100%);
  }
  .card--front { left: 630px; top: 340px; }
  .sky-photo {
    position: absolute; inset: 0;
    background:
      radial-gradient(ellipse 40% 22% at 70% 15%, rgba(255,255,255,0.7), transparent 70%),
      radial-gradient(ellipse 35% 18% at 20% 45%, rgba(255,255,255,0.5), transparent 70%),
      linear-gradient(180deg, #8fb8e6 0%, #b4d0ef 55%, var(--card-white) 100%);
  }
  .art { position: absolute; }
  .art--butterfly-single {
    left: 380px; top: 22px; width: 46px; height: 32px; border-radius: 40%;
    background: radial-gradient(circle, var(--butterfly-blue), #1d5d8c);
  }
  .art--hand-butterflies {
    left: 365px; top: 150px; width: 155px; height: 90px;
    border-radius: 30px 0 0 30px;
    background: linear-gradient(100deg, rgba(50,120,190,0.55) 0%, rgba(58,166,216,0.45) 40%, var(--hand-tone) 72%, #d9a47c 100%);
  }
  .brand {
    position: absolute; font-family: "Kaushan Script", cursive;
    color: var(--title-blue); font-size: 32px; letter-spacing: 3px; line-height: 40px;
  }
  .tagline {
    position: absolute; font-family: "Kaushan Script", cursive;
    color: var(--tagline-blue); font-size: 24px; line-height: 30px; white-space: nowrap;
  }
  .card--back .brand { left: 190px; top: 60px; }
  .card--back .tagline { left: 55px; top: 108px; }
  .services {
    position: absolute; left: 140px; top: 170px; list-style: none;
    font-family: "Didact Gothic", sans-serif; font-size: 17px; color: var(--ink);
  }
  .services li { display: flex; align-items: center; gap: 10px; line-height: 28px; }
  .services svg { width: 12px; height: 10px; fill: var(--tagline-blue); }
  .card--front .brand { left: 150px; top: 52px; }
  .card--front .tagline { left: 60px; top: 98px; }
  .contact {
    position: absolute; left: 150px; top: 195px;
    font-family: "Didact Gothic", sans-serif; color: var(--ink);
  }
  .contact__name { font-size: 18px; color: var(--tagline-blue); }
  .contact__role { font-size: 14px; margin: 3px 0 4px; }
  .contact__line { display: flex; align-items: center; gap: 7px; font-size: 14px; line-height: 20px; }
  .contact__line svg { width: 12px; height: 12px; fill: var(--tagline-blue); }
</style>
</head>
<body>
<main class="stage">
  <section class="card card--back" aria-label="Business card back">
    <div class="art art--butterfly-single" role="img" aria-label="Blue butterfly illustration"></div>
    <div class="brand">PEBBLES”</div>
    <div class="tagline">A Warm Hearth To Rest When You Tire</div>
    <ul class="services">
      <li><svg viewBox="0 0 12 10"><path d="M0 0 L12 5 L0 10 L3 5 Z"/></svg>Hypnosis</li>
      <li><svg viewBox="0 0 12 10"><path d="M0 0 L12 5 L0 10 L3 5 Z"/></svg>Aromatherapy</li>
      <li><svg viewBox="0 0 12 10"><path d="M0 0 L12 5 L0 10 L3 5 Z"/></svg>Listen Therapy</li>
    </ul>
  </section>

  <section class="card card--front" aria-label="Business card front">
    <div class="sky-photo" role="img" aria-label="Photograph of a soft blue sky with light clouds"></div>
    <div class="art art--hand-butterflies" role="img" aria-label="Photograph of an open hand releasing three blue butterflies"></div>
    <div class="brand">PEBBLES”</div>
    <div class="tagline">A Warm Hearth To Rest When You Tire</div>
    <div class="contact">
      <div class="contact__name">Marisol T Fenwhistle</div>
      <div class="contact__role">Release Therapist</div>
      <div class="contact__line">
        <svg viewBox="0 0 24 24"><path d="M6.6 10.8a15 15 0 0 0 6.6 6.6l2.2-2.2a1 1 0 0 1 1-.25 11.4 11.4 0 0 0 3.6.57 1 1 0 0 1 1 1V20a1 1 0 0 1-1 1A17 17 0 0 1 3 4a1 1 0 0 1 1-1h3.5a1 1 0 0 1 1 1c0 1.25.2 2.45.57 3.57a1 1 0 0 1-.25 1z"/></svg>
        0482 516 904
      </div>
      <div class="contact__line">
        <svg viewBox="0 0 24 24"><path d="M2 5h20v14H2z M2 5l10 8 10-8" stroke="#fff" stroke-width="1.5"/></svg>
        calmingpaths4you@quietmail.example
      </div>
    </div>
  </section>
</main>
</body>
</html>
```